Flyer für den Bereich Solarenergie
Zielgruppe
Guten Tag,
wir sind im Bereich Solarenergie tätig. Wir suchen nun Hallen mit großen Dächern, die wir anmieten können, um darauf Solaranlagen zu bauen. Wir machen dabei alles aus einer Hand. der Eigentümer muss nichts machen. Er bekommt sogar Geld von uns und das Dach ist sowieso meistens leer.
Aufgabenstellung
Wir möchten einen DINA4 Flyer den wir als PDF in Emails verschicken können. Farbdaten sollten Sie aus den Logodateien im Anhang entnehmen können. Richten Sie sich auch gerne an das Design des Logos und der Website. Dabei sollen kurz die wichtigsten Key Faktoren aufgelistet werden und das Unternehmen kurz dargestellt werden. Hier einmal die Texte:
Beschreibung zum Unternehmen:
Veltrano ist Experte für grüne Energietechnik mit über 20 Jahren Erfahrung. Mit über 1.000 zufriedenen Kunden im Bereich Photovoltaikanlagen können wir auf einen großen Erfahrungsschatz zurückgreifen. Wenn wir am Werk sind, wird nicht nur das Klima geschont, sondern auch Sie als Kunde profitieren. Mit uns wird nachhaltiges Handeln kinderleicht und gleichzeitig rentabel.
Erwirtschaften auch Sie mit Ihrem Dach nun bares Geld!
Ihre Vorteile:
- Umwelt schonen durch das Produzieren von grünem Strom
- Dach schützen vor Emissionen
- Dachsanierungen anstatt von Mietzahlungen möglich
- Keine Kosten, da wir alle Kosten der Anträge, der Anlage und aller Arbeiten übernehmen
- Mieteinnahmen generieren!
Einzige Voraussetzung:
Dachfläche mit mind. 1.500qm
Worauf warten Sie?
Nehmen Sie jetzt Kontakt auf für eine entsprechende Machbarkeitsprüfung. Natürlich ist auch das Kostenlos.
veltrano GmbH
Fennstraße 47b
48155 Münster
T: +49 176 528 914 03
E: info@veltrano-beispiel.de

```html
<!DOCTYPE html>
<html lang="de">
<head>
<meta charset="utf-8">
<title>veltrano Energietechnik – Flyer Solardach</title>
<link href="https://fonts.googleapis.com/css2?family=Poppins:wght@600;700&family=Didact+Gothic&family=Questrial&display=swap" rel="stylesheet">
<style>
  :root {
    --green: #9cb83a;
    --green-mid: #8aa034;
    --olive: #5e5a2b;
    --olive-dark: #4d4820;
    --icon: #7d9a35;
    --text: #5b5632;
    --white: #ffffff;
  }
  * { margin: 0; padding: 0; box-sizing: border-box; }
  html, body { width: 848px; height: 1200px; overflow: hidden; background: var(--white); }
  .flyer { position: relative; width: 848px; height: 1200px; overflow: hidden; background: var(--white); font-family: "Didact Gothic", sans-serif; color: var(--text); }
  .layer { position: absolute; left: 0; top: 0; width: 848px; height: 1200px; }
  .brand { position: absolute; left: 38px; top: 24px; }
  .brand-name { font-family: "Questrial", sans-serif; font-size: 40px; line-height: 40px; color: var(--olive); letter-spacing: -0.5px; }
  .brand-sub { font-family: "Questrial", sans-serif; font-size: 9.5px; letter-spacing: 4.2px; color: var(--olive); margin-top: 4px; margin-left: 2px; }
  .headline { position: absolute; left: 40px; top: 109px; font-family: "Poppins", sans-serif; font-weight: 700; font-size: 40px; line-height: 51px; color: var(--white); letter-spacing: 0.2px; }
  .benefits { position: absolute; left: 34px; top: 0; width: 400px; }
  .benefit { position: absolute; left: 0; width: 400px; display: flex; align-items: center; }
  .benefit-icon { width: 68px; height: 68px; flex: none; }
  .benefit-copy { position: absolute; left: 86px; top: -8px; }
  .benefit-title { font-family: "Poppins", sans-serif; font-weight: 700; font-size: 18px; color: var(--olive-dark); line-height: 26px; }
  .benefit-text { font-size: 22px; line-height: 24px; color: var(--text); }
  .contact-bar { position: absolute; left: 0; top: 1040px; width: 848px; height: 77px; background: var(--green); }
  .contact-bar::before { content: ""; position: absolute; left: 0; top: 0; width: 19px; height: 77px; background: var(--green-mid); }
  .contact-call { position: absolute; left: 41px; top: 14px; font-family: "Poppins", sans-serif; font-weight: 700; font-size: 17.5px; line-height: 24px; color: var(--white); }
  .contact-divider { position: absolute; left: 431px; top: 14px; width: 1px; height: 52px; background: rgba(255,255,255,0.8); }
  .contact-list { position: absolute; left: 491px; top: 14px; list-style: none; }
  .contact-list li { display: flex; align-items: center; gap: 12px; font-family: "Poppins", sans-serif; font-weight: 700; font-size: 17.5px; line-height: 24px; color: var(--white); }
  .contact-list svg { width: 20px; height: 20px; }
  .website { position: absolute; left: 41px; top: 1142px; font-family: "Poppins", sans-serif; font-weight: 700; font-size: 20px; line-height: 30px; color: var(--olive-dark); letter-spacing: 0; white-space: nowrap; }
</style>
</head>
<body>
<main class="flyer">
  <svg class="layer" viewBox="0 0 848 1200" role="img" aria-label="Foto: Einfamilienhaus mit Solarmodulen auf rotem Ziegeldach, Zaun und blauem Himmel">
    <defs>
      <linearGradient id="houseGrad" x1="0" y1="0" x2="0" y2="1">
        <stop offset="0" stop-color="#8cbfe6"/><stop offset="0.45" stop-color="#c8643a"/><stop offset="0.7" stop-color="#7a8c48"/><stop offset="1" stop-color="#c9c9c4"/>
      </linearGradient>
    </defs>
    <polygon points="527,0 848,0 848,373 469,373" fill="url(#houseGrad)"/>
  </svg>
  <svg class="layer" viewBox="0 0 848 1200" role="img" aria-label="Foto: zwei Monteure mit Schutzhelm und Klemmbrett auf einem Dach mit Solarmodulen">
    <defs>
      <linearGradient id="crewGrad" x1="0" y1="0" x2="1" y2="1">
        <stop offset="0" stop-color="#dfe3e8"/><stop offset="0.5" stop-color="#b8c0c8"/><stop offset="1" stop-color="#8d6a4a"/>
      </linearGradient>
    </defs>
    <polygon points="465,383 848,383 848,785 400,785" fill="url(#crewGrad)"/>
  </svg>
  <svg class="layer" viewBox="0 0 848 1200" role="img" aria-label="Foto: Monteur installiert blaue Solarmodule auf einem Dach unter blauem Himmel">
    <defs>
      <linearGradient id="roofGrad" x1="0" y1="0" x2="0" y2="1">
        <stop offset="0" stop-color="#7fb0dc"/><stop offset="0.45" stop-color="#3d5fa8"/><stop offset="1" stop-color="#1f3a8a"/>
      </linearGradient>
    </defs>
    <polygon points="400,795 841,795 804,1040 362,1040" fill="url(#roofGrad)"/>
  </svg>
  <svg class="layer" viewBox="0 0 848 1200" role="img" aria-label="Foto: Ausschnitt blauer Solarmodule auf einem Dach">
    <defs>
      <linearGradient id="panelGrad" x1="0" y1="0" x2="1" y2="0">
        <stop offset="0" stop-color="#6a5446"/><stop offset="0.25" stop-color="#2a4696"/><stop offset="1" stop-color="#3552a8"/>
      </linearGradient>
    </defs>
    <polygon points="342,1117 790,1117 778,1200 334,1200" fill="url(#panelGrad)"/>
  </svg>

  <svg class="layer" viewBox="0 0 848 1200" aria-hidden="true">
    <polygon points="325,51 522,31 513,96" fill="var(--olive)"/>
    <polygon points="325,51 513,96 537,101 316,101" fill="var(--green-mid)"/>
    <polygon points="0,101 537,101 513,222 0,222" fill="var(--green)"/>
  </svg>

  <header class="brand">
    <div class="brand-name">veltrano</div>
    <div class="brand-sub">ENERGIETECHNIK</div>
  </header>

  <h1 class="headline">Verdienen Sie bares<br>Geld mit Ihrem Dach!</h1>

  <section class="benefits">
    <div class="benefit" style="top:278px">
      <svg class="benefit-icon" viewBox="0 0 68 68" aria-hidden="true"><circle cx="34" cy="34" r="34" fill="var(--icon)"/><path d="M14 44c6-1 10 1 14 1h10c2 0 2-3 0-3h-8M14 44l8-6c3-2 6-2 9 0h6" fill="none" stroke="#fff" stroke-width="1.6" stroke-linecap="round"/><path d="M34 36c-1-8 4-13 12-13-1 8-5 12-12 13zM34 36c-4-2-7-6-6-11 5 1 7 5 6 11z" fill="none" stroke="#fff" stroke-width="1.6"/></svg>
      <div class="benefit-copy"><div class="benefit-title">Umweltschutz</div><div class="benefit-text">Umwelt schonen durch das<br>Produzieren von grünem Strom.</div></div>
    </div>
    <div class="benefit" style="top:414px">
      <svg class="benefit-icon" viewBox="0 0 68 68" aria-hidden="true"><circle cx="34" cy="34" r="34" fill="var(--icon)"/><circle cx="34" cy="30" r="12" fill="none" stroke="#fff" stroke-width="1.6"/><path d="M22 30h24M34 18c-5 6-5 18 0 24M34 18c5 6 5 18 0 24" fill="none" stroke="#fff" stroke-width="1.2"/><path d="M14 30l3 14 7 6M54 30l-3 14-7 6" fill="none" stroke="#fff" stroke-width="1.6" stroke-linecap="round"/></svg>
      <div class="benefit-copy"><div class="benefit-title">Nachhaltig</div><div class="benefit-text">Ihr Dach ist vor Emissionen<br>geschützt.</div></div>
    </div>
    <div class="benefit" style="top:543px">
      <svg class="benefit-icon" viewBox="0 0 68 68" aria-hidden="true"><circle cx="34" cy="34" r="34" fill="var(--icon)"/><rect x="20" y="13" width="28" height="42" rx="2" fill="none" stroke="#fff" stroke-width="1.6"/><g stroke="#fff" stroke-width="1.4" fill="none"><circle cx="26" cy="23" r="2"/><circle cx="26" cy="30" r="2"/><circle cx="26" cy="37" r="2"/><circle cx="26" cy="44" r="2"/><path d="M31 23h12M31 30h12M31 37h12M31 44h12"/></g></svg>
      <div class="benefit-copy"><div class="benefit-title">Planbar</div><div class="benefit-text">Dachsanierungen anstatt<br>von Mietzahlungen möglich.</div></div>
    </div>
    <div class="benefit" style="top:668px">
      <svg class="benefit-icon" viewBox="0 0 68 68" aria-hidden="true"><circle cx="34" cy="34" r="34" fill="var(--icon)"/><g fill="none" stroke="#fff" stroke-width="1.6"><rect x="17" y="26" width="26" height="8"/><rect x="19" y="34" width="22" height="18"/><path d="M30 26v26M30 26c-4-8-10-6-8-2 1 2 5 2 8 2zM30 26c4-8 10-6 8-2-1 2-5 2-8 2z"/><rect x="40" y="34" width="14" height="9" transform="rotate(40 47 38)"/></g></svg>
      <div class="benefit-copy"><div class="benefit-title">Kostenfrei</div><div class="benefit-text">Wir übernehmen alle Kosten<br>der Anträge, der Anlage<br>und aller Arbeiten.</div></div>
    </div>
    <div class="benefit" style="top:808px">
      <svg class="benefit-icon" viewBox="0 0 68 68" aria-hidden="true"><circle cx="34" cy="34" r="34" fill="var(--icon)"/><path d="M29 22h10l-2-6h-6zM29 22c-10 6-12 26 5 26s15-20 5-26z" fill="#fff"/><text x="34" y="43" text-anchor="middle" font-family="Poppins, sans-serif" font-size="13" font-weight="700" fill="var(--icon)">€</text></svg>
      <div class="benefit-copy"><div class="benefit-title">Zuverdienst</div><div class="benefit-text">Sie generieren durch uns<br>Mieteinnahmen.</div></div>
    </div>
    <div class="benefit" style="top:936px">
      <svg class="benefit-icon" viewBox="0 0 68 68" aria-hidden="true"><circle cx="34" cy="34" r="34" fill="var(--icon)"/><path d="M6 40l26-15 30 17M12 34v-6h3v4M20 38l12-8 16 9" fill="none" stroke="#fff" stroke-width="1.5"/></svg>
      <div class="benefit-copy"><div class="benefit-title">Voraussetzung</div><div class="benefit-text">Dachfläche mit mind.<br>1.500qm.</div></div>
    </div>
  </section>

  <footer class="contact-bar">
    <p class="contact-call">Kontaktieren Sie uns jetzt für eine<br>kostenlose Machbarkeitsprüfung!</p>
    <span class="contact-divider"></span>
    <ul class="contact-list">
      <li><svg viewBox="0 0 20 20" aria-hidden="true"><path d="M4 2l4 4-2 3c1 2 3 4 5 5l3-2 4 4-3 3C8 19 1 12 1 5z" fill="#fff"/></svg>+49 176 528 914 03</li>
      <li><svg viewBox="0 0 20 20" aria-hidden="true"><rect x="1" y="4" width="18" height="13" fill="#fff"/><path d="M1 4l9 7 9-7M1 17l7-6M19 17l-7-6" fill="none" stroke="var(--green)" stroke-width="1.5"/></svg>info@veltrano-beispiel.de</li>
    </ul>
  </footer>

  <div class="website">www.veltrano-beispiel.de</div>
</main>
</body>
</html>
```